need a clean, modern job advertisement designed for social media (Facebook & Instagram).

The post is to advertise two positions:
• Leading Hand Boilermaker
• Dragline Fitter
We want the design to match our KRT Plant Services branding: blue, white, strong, professional, mining-industry style.
What the design should include:
Bold headline: “WE’RE HIRING”
Sub-headline: “Leading Hand Boilermaker & Dragline Fitter”
Key points:
• Bowen Basin based
• Dragline & shovel maintenance
• Great pay + long-term work
• Locally owned & operated
KRT logo placed cleanly
Space for 1–2 images (boilermaking or dragline work)
Design style:
Strong and industrial
Blue/white colour scheme
Easy to read at a glance
Suitable for a square 1080×1080 design

```html
<!DOCTYPE html>
<html lang="en">
<head>
<meta charset="utf-8">
<title>KRT Plant Services – We're Hiring</title>
<link rel="stylesheet" href="https://fonts.googleapis.com/css2?family=Bebas+Neue&family=Montserrat:ital,wght@0,700;0,800;1,800&display=swap">
<style>
  :root {
    --sky: #16a9e1;
    --sun: #f8c90c;
    --steel: #616569;
    --navy-accent: #3b6fb6;
    --ink: #111111;
    --paper: #ffffff;
    --brown: #4a2a14;
  }
  * { margin: 0; padding: 0; box-sizing: border-box; }
  html, body { width: 960px; height: 1200px; overflow: hidden; background: var(--paper); }
  .poster { position: relative; width: 960px; height: 1200px; overflow: hidden; background: var(--paper); font-family: "Montserrat", Arial, sans-serif; }

  .yellow-column { position: absolute; left: 567px; top: 0; width: 285px; height: 1200px; background: var(--sun); }
  .yellow-strip { position: absolute; left: 40px; top: 867px; width: 34px; height: 333px; background: var(--sun); z-index: 2; }

  .accent { position: absolute; background: var(--navy-accent); }
  .accent-top { left: 815px; top: 324px; width: 125px; height: 125px; }
  .accent-bottom { left: 613px; top: 707px; width: 125px; height: 124px; }

  .photo { position: absolute; }
  .photo-welding { left: 620px; top: 33px; width: 307px; height: 400px;
    background: radial-gradient(circle at 68% 40%, #cfd6e6 0%, #5c6478 14%, #23242e 45%, #15151c 100%); }
  .photo-crew { left: 628px; top: 472px; width: 286px; height: 342px;
    background: linear-gradient(160deg, #c9ccd1 0%, #8d9098 40%, #6b5f55 70%, #4a4a4c 100%); }

  .brand { position: absolute; left: 200px; top: 168px; width: 330px; display: flex; align-items: center; justify-content: center; gap: 12px; }
  .brand-mark { width: 22px; height: 22px; background: var(--sky); }
  .brand-name { font-family: "Montserrat", Arial, sans-serif; font-weight: 800; font-size: 30px; color: var(--sky); white-space: nowrap; }

  .headline { position: absolute; right: 429px; text-align: right; font-family: "Bebas Neue", Impact, sans-serif; line-height: 1; }
  .headline-were { top: 326px; font-size: 192px; color: var(--steel); letter-spacing: -2px; }
  .headline-hiring { top: 470px; font-size: 256px; color: var(--sky); letter-spacing: -6px; text-shadow: 7px 7px 0 var(--ink); }

  .roles { position: absolute; right: 429px; top: 676px; text-align: right; font-weight: 800; font-size: 39px; line-height: 48px; color: var(--ink); }

  .info-band { position: absolute; left: 0; top: 850px; width: 960px; height: 265px; }

  .cta { position: absolute; }
  .cta-megaphone { left: 93px; top: 915px; width: 130px; height: 125px; border-radius: 18px;
    background: linear-gradient(135deg, #fbd34a 0%, #f0b400 100%); }
  .cta-join { left: 213px; top: 982px; width: 138px; height: 40px; background: var(--sun);
    font-weight: 800; font-size: 34px; line-height: 40px; text-align: center; color: var(--brown); letter-spacing: 2px; }
  .cta-now { left: 147px; top: 1022px; width: 186px; height: 67px; background: var(--brown);
    font-weight: 800; font-size: 52px; line-height: 67px; text-align: center; color: var(--paper); }

  .perks { position: absolute; left: 392px; top: 911px; list-style: none; font-weight: 700; font-size: 31px; line-height: 38.5px; color: var(--ink); }
  .perks li::before { content: "•"; margin-right: 6px; }

  .website { position: absolute; left: 124px; top: 1125px; font-weight: 800; font-style: italic; font-size: 41px; color: var(--ink); letter-spacing: -0.5px; z-index: 3; }
</style>
</head>
<body>
<main class="poster">
  <div class="yellow-column"></div>

  <div class="accent accent-top"></div>
  <div class="photo photo-welding" role="img" aria-label="Boilermaker in hi-vis welding inside dragline structure"></div>

  <div class="accent accent-bottom"></div>
  <div class="photo photo-crew" role="img" aria-label="Fitters in hard hats working on a dragline boom under scaffolding"></div>

  <div class="brand">
    <span class="brand-mark"></span>
    <span class="brand-name">KRT Plant Services</span>
  </div>

  <h1>
    <span class="headline headline-were">WE’RE</span>
    <span class="headline headline-hiring">HIRING</span>
  </h1>

  <p class="roles">Leading<br>Hand Boilermaker<br>&amp; Dragline Fitter</p>

  <svg class="info-band" width="960" height="265" viewBox="0 0 960 265" aria-hidden="true">
    <polygon points="0,3 173,34 311,3 960,3 960,265 0,265" fill="var(--sky)"/>
    <polyline points="0,3 173,34 311,3 960,3" fill="none" stroke="var(--ink)" stroke-width="5"/>
  </svg>

  <div class="yellow-strip"></div>

  <div class="cta cta-megaphone" role="img" aria-label="Megaphone illustration"></div>
  <div class="cta cta-join">JOIN</div>
  <div class="cta cta-now">NOW</div>

  <ul class="perks">
    <li>Bowen Basin based</li>
    <li>Dragline &amp; shovel maintenance</li>
    <li>Great pay + long-term work</li>
    <li>Locally owned &amp; operated</li>
  </ul>

  <p class="website">www.krtplantservices.com</p>
</main>
</body>
</html>
```